Web Design Project

Goal
Combine 2 sites into 1 and enhance functionality

Concept & Overview

My current websites are ewanorates dot com and pathandpeers dot org. They are not very popular but I run ads and capture leads and do a tidy bit, but I am going on tour and need to have my website upgrade.

My goal is to redesign ewanorates and have it as a 10 page site that introduces me and also capture leads in an effective manner then introduce a 5 page system.

I need to update the layout and feel of the site to match the color and image of the book. Currently the book is at pathandpeers.org and my speaking is at ewanorates.com. I need the two to combine but I also need functionality to improve. I introduce a 5 step system and I think a visual image like this one can better introduce it.

Here: https://www.velmora.com/packages/kxt-dana-orwells-daily-renewal-course.html

Then in there I need the Lesson Area

Like:

https://www.velmora.com/packages/kxt-dana-orwells-daily-renewal-course.html

They are few samples I can show but this is the main concept.

Target Market(s)

Schools, colleges, churches, and youth organizations

Industry/Entity Type

Tour

Requirements
Must have
• A clean wide home page that is properly designed can do the job of leading to the optin without the sales look.

Nice to have
• https://www.velmora.com/packages/kxt-dana-orwells-daily-renewal-course.html
Should not have
• Sales look and feel

```html
<!DOCTYPE html>
<html lang="en">
<head>
<meta charset="utf-8">
<title>Ewan Halvorsen — Youth Speaker</title>
<link href="https://fonts.googleapis.com/css2?family=Arimo:wght@400;700&family=Dancing+Script:wght@600&family=Kaushan+Script&display=swap" rel="stylesheet">
<style>
:root{
  --navy:#1f22a6;
  --navy-dark:#15188a;
  --sky:#8fd0f5;
  --sky-light:#cbeafc;
  --panel:#1f95e8;
  --orange:#f8a93b;
  --orange-dark:#f08a1d;
  --red:#d3210f;
  --ink:#333;
  --muted:#555;
  --grey-band:#f2f2f2;
  --footer:#e9e9e9;
  --green:#8fcf4a;
  --green-dark:#5ea52a;
  --white:#fff;
}
*{box-sizing:border-box;margin:0;padding:0}
html,body{width:805px;height:1200px;overflow:hidden;background:var(--white);font-family:"Arimo",Arial,sans-serif;color:var(--ink)}
.page{position:relative;width:805px;height:1200px}
.abs{position:absolute}
.masthead{left:0;top:0;width:805px;height:57px;background:linear-gradient(90deg,var(--navy-dark),#2a36c4 60%,#4d63d8)}
.brand{left:146px;top:12px;font-family:"Dancing Script",cursive;font-size:25px;color:var(--white)}
.birds{left:594px;top:4px;width:80px;height:46px;background:rgba(255,255,255,.18);border-radius:6px}
.nav{left:0;top:57px;width:805px;height:33px;background:linear-gradient(#2b2fbf,var(--navy));border-top:1px solid #4a56d6}
.nav a{position:absolute;top:12px;font-size:7.5px;font-weight:700;color:var(--white);text-decoration:none;white-space:nowrap}
.nav .current{left:143px;top:0;width:91px;height:30px;background:linear-gradient(#ffc25a,var(--orange-dark));text-align:center;padding-top:12px}
.hero{left:0;top:90px;width:805px;height:168px;background:linear-gradient(180deg,var(--sky),var(--sky-light) 60%,#e6f5fe)}
.hero-card{left:143px;top:100px;width:527px;height:152px;background:linear-gradient(180deg,#35a9f2,var(--panel));border:1px solid #6cc2f6}
.portrait{left:150px;top:108px;width:88px;height:86px;background:linear-gradient(#777,#2a2a2a);border:2px solid var(--white)}
.hero-name{left:150px;top:198px;font-family:"Dancing Script",cursive;font-size:13px;color:var(--white)}
.roles{left:151px;top:217px;list-style:none;font-size:7px;font-weight:700;color:var(--white);line-height:9px}
.roles li::before{content:"➔ ";}
.hero-quote{left:248px;top:113px;width:420px;font-size:12px;font-weight:700;color:var(--white);line-height:15px;letter-spacing:-.1px}
.hero-copy{left:248px;top:158px;width:412px;font-size:7px;line-height:9px;color:var(--white)}
.hero-copy p{margin-bottom:6px}
.readmore{left:248px;top:226px;width:58px;height:14px;border-radius:8px;background:#1577c9;color:var(--white);font-size:7px;font-weight:700;padding:3px 0 0 6px}
.section-title{font-family:"Kaushan Script",cursive;font-size:11px;color:var(--muted);font-weight:400;white-space:nowrap}
.video{left:143px;top:293px;width:364px;height:203px;background:linear-gradient(180deg,#0c0c0c 15%,#5a4a3a 45%,#2b2520 80%,#000)}
.vbar{left:147px;top:470px;width:355px;height:20px;background:#111}
.vplay{left:149px;top:471px;width:36px;height:18px;background:#2a2a2a}
.vtrack{left:197px;top:478px;width:262px;height:5px;border:1px solid #555;border-radius:3px}
.vtime{left:187px;top:468px;font-size:6px;color:#ccc;background:#000;padding:0 2px}
.optin-head{left:515px;top:293px;width:154px;height:36px;background:linear-gradient(#3a3fd0,var(--navy));color:var(--white);font-size:9.5px;font-weight:700;padding:5px 8px;line-height:12px}
.cap{left:626px;top:265px;width:56px;height:40px}
.optin-body{left:515px;top:329px;width:154px;height:126px;background:linear-gradient(var(--orange),#f7c063)}
.label{font-family:"Kaushan Script",cursive;font-size:9px;color:var(--red)}
.field{width:122px;height:13px;background:var(--white);border:1px solid #d88b25}
.optin-btn{left:523px;top:417px;width:139px;height:24px;border-radius:12px;background:linear-gradient(#ee4a2a,#b8160a);font-family:"Kaushan Script",cursive;font-size:10px;color:var(--white);text-align:center;padding-top:5px}
.optin-foot{left:515px;top:455px;width:154px;height:41px;background:#111;color:var(--white);font-size:6.5px;font-weight:700;line-height:8px;padding:13px 8px 0}
.book-band{left:0;top:512px;width:805px;height:123px;background:var(--grey-band);border-bottom:1px solid #ddd}
.book-art{left:153px;top:515px;width:128px;height:103px;background:linear-gradient(135deg,#2d6fb0,#9cc3e2 60%,#eee);border-radius:4px}
.book-title{left:297px;top:532px;font-size:11px}
.isbn{left:297px;top:549px;font-size:5px;font-weight:700;color:var(--muted)}
.book-copy{left:297px;top:561px;width:374px;font-size:6.5px;line-height:8.5px;color:var(--muted)}
.book-copy p{margin-bottom:7px}
.item-num{width:17px;height:17px;border-radius:50%;background:#555;color:var(--white);font-size:11px;font-weight:700;text-align:center;line-height:17px}
.item-icon{width:51px;height:58px;border:1px solid #ddd;border-radius:5px;background:linear-gradient(#fff,#eee)}
.item-icon .disc{position:absolute;left:12px;top:15px;width:27px;height:27px;border-radius:50%;background:radial-gradient(circle,#fff 18%,#bbb 20%,#e9e9e9 55%,#cfcfcf)}
.item-icon .doc{position:absolute;left:13px;top:8px;width:26px;height:40px;background:var(--white);border:1px solid #ccc}
.item-icon .doc::before{content:"";position:absolute;left:-4px;top:6px;width:20px;height:8px;background:#d92a1e}
.item-label{font-size:10px;font-weight:700;color:var(--muted);line-height:12px}
.join{left:144px;top:907px;width:526px;height:25px;border-radius:6px;background:linear-gradient(#b5e47a,var(--green));border:1px solid var(--green-dark);font-family:"Kaushan Script",cursive;font-size:11px;color:#2d6d11;text-align:center;padding-top:4px}
.footer{left:0;top:955px;width:805px;height:170px;background:var(--footer);border-top:1px solid #ccc}
.testimonials{left:153px;top:956px;width:266px;height:166px;background:linear-gradient(var(--white),#f4f4f4)}
.quote{font-size:6.5px;line-height:8px;color:var(--muted);width:245px}
.cite{font-size:6.5px;font-weight:700;color:var(--muted)}
.rule{height:0;border-top:1px dotted #aaa}
.fcol h4{font-family:"Kaushan Script",cursive;font-weight:400;font-size:10px;color:var(--muted)}
.fcol p{font-size:6.5px;color:var(--muted);line-height:13px}
.social{width:30px;height:30px;border-radius:50%;background:linear-gradient(#f4f4f4,#c8c8c8);border:1px solid #bbb}
.copyright{left:153px;top:1127px;font-size:6.5px;color:var(--muted)}
.foot-bar{left:0;top:1124px;width:805px;height:16px;background:#f3f3f3}
</style>
</head>
<body>
<div class="page">
  <header>
    <div class="abs masthead"></div>
    <div class="abs brand">Ewan Halvorsen</div>
    <div class="abs birds" role="img" aria-label="Flock of white doves in flight"></div>
    <nav class="abs nav">
      <a class="current" href="#">EWAN HALVORSEN</a>
      <a href="#" style="left:255px">ABOUT</a>
      <a href="#" style="left:302px">SPEAKING</a>
      <a href="#" style="left:365px">PRODUCTS</a>
      <a href="#" style="left:440px">PROGRAMS</a>
      <a href="#" style="left:504px">MENTORING</a>
      <a href="#" style="left:567px">TESTIMONIALS</a>
      <a href="#" style="left:636px">CONTACT</a>
    </nav>
  </header>

  <section class="hero-section">
    <div class="abs hero" role="img" aria-label="Bright sky with soft clouds"></div>
    <div class="abs hero-card"></div>
    <div class="abs portrait" role="img" aria-label="Black and white portrait of Ewan Halvorsen"></div>
    <div class="abs hero-name">Ewan Halvorsen</div>
    <ul class="abs roles"><li>Youth Expert</li><li>Motivational Speaker</li><li>Author</li></ul>
    <h1 class="abs hero-quote">"From a high school dropout to a high school valedictorian, ewan's goal is to show students how to get back on track"</h1>
    <div class="abs hero-copy">
      <p>Ewan is a youth expert- an author, youth motivational speaker and teen leader who understands the journey of many students today. The former gang member and high school drop out understands the challenges faced by students who are seeking approval and acceptance.</p>
      <p>His journey from gang member to high school teacher was long but gave empowerment and challenges students to make choices, build character and live their best life.</p>
    </div>
    <a class="abs readmore">Read more &nbsp;▸</a>
  </section>

  <section class="video-section">
    <h2 class="abs section-title" style="left:143px;top:270px">Video presentation</h2>
    <div class="abs video" role="img" aria-label="Video still of Ewan speaking to a classroom audience"></div>
    <div class="abs vbar"></div>
    <div class="abs vplay"><svg width="36" height="18"><path d="M15 5 L23 9 L15 13 Z" fill="#fff"/></svg></div>
    <div class="abs vtrack"></div>
    <div class="abs vtime">13:49</div>

    <div class="abs optin-head">Get Ewan's Free<br>Ebook on Helping Teens</div>
    <div class="abs cap" role="img" aria-label="Graduation cap"><svg width="56" height="40"><path d="M2 12 L34 2 L54 16 L22 28 Z" fill="#1b24a8"/></svg></div>
    <div class="abs optin-body"></div>
    <div class="abs label" style="left:523px;top:340px">First name :</div>
    <div class="abs field" style="left:523px;top:355px"></div>
    <div class="abs label" style="left:523px;top:377px">Email address :</div>
    <div class="abs field" style="left:523px;top:392px"></div>
    <div class="abs optin-btn">get me the free ebook</div>
    <div class="abs optin-foot">To know more about the training programs we offer please click here</div>
  </section>

  <section class="book-section">
    <div class="abs book-band"></div>
    <div class="abs book-art" role="img" aria-label="Book covers, open workbook and CDs"></div>
    <h2 class="abs section-title book-title">About book : life's open road</h2>
    <div class="abs isbn">ISBN: 978-0-5512-8846-3</div>
    <div class="abs book-copy">
      <p>Life's Open Road &nbsp;the inspirational story of MJ, a young man struggling with realizing his full potential. After getting into a fight at school, MJ begins to reprioritize his goals and reevaluate where he wants his life to go. He joins a leadership course initially to earn an easy A, but soon forms a bond with a mentor while on a class trip.</p>
      <p>In meeting this mentor, MJ learns of ways to improve his life and attitude, giving him a new lease on life.</p>
    </div>
  </section>

  <section class="program-section">
    <h2 class="abs section-title" style="left:143px;top:645px">What you get when you join the program</h2>

    <div class="abs item-num" style="left:143px;top:675px">1</div>
    <div class="abs item-icon" style="left:170px;top:675px"><span class="disc"></span></div>
    <div class="abs item-label" style="left:228px;top:692px">30 Min. DVD</div>

    <div class="abs item-num" style="left:415px;top:675px">2</div>
    <div class="abs item-icon" style="left:443px;top:675px"><span class="doc"></span></div>
    <div class="abs item-label" style="left:508px;top:692px">Interactive Q&amp;A Sticker Pack</div>

    <div class="abs item-num" style="left:143px;top:746px">3</div>
    <div class="abs item-icon" style="left:170px;top:746px"><span class="doc"></span></div>
    <div class="abs item-label" style="left:228px;top:754px">Discover Your Identity Guide<br>Book</div>

    <div class="abs item-num" style="left:415px;top:746px">4</div>
    <div class="abs item-icon" style="left:443px;top:746px"><span class="disc"></span></div>
    <div class="abs item-label" style="left:508px;top:754px">Resource CD #1</div>

    <div class="abs item-num" style="left:143px;top:821px">5</div>
    <div class="abs item-icon" style="left:170px;top:821px"><span class="disc"></span></div>
    <div class="abs item-label" style="left:228px;top:828px">Resource CD #2</div>

    <div class="abs item-num" style="left:415px;top:821px">6</div>
    <div class="abs item-icon" style="left:443px;top:821px"><span class="disc"></span></div>
    <div class="abs item-label" style="left:508px;top:828px">Resource CD #3</div>

    <div class="abs join">Join the program</div>
  </section>

  <footer>
    <div class="abs footer"></div>
    <div class="abs testimonials"></div>
    <h3 class="abs section-title" style="left:166px;top:970px">Testimonials</h3>
    <p class="abs quote" style="left:166px;top:987px">Profit in business comes from repeat customers, customers that boast about your project or service, and that bring friends with them.</p>
    <p class="abs cite" style="left:166px;top:1008px">R. Talbot Greene</p>
    <div class="abs rule" style="left:166px;top:1027px;width:240px"></div>
    <p class="abs quote" style="left:166px;top:1037px">Profit in business comes from repeat customers, customers that boast about your project or service, and that bring friends with them.</p>
    <p class="abs cite" style="left:166px;top:1058px">R. Talbot Greene</p>

    <div class="abs fcol" style="left:435px;top:970px"><h4>Contact Us</h4><p>Phone<br>Email</p></div>
    <div class="abs fcol" style="left:501px;top:970px"><h4>Speaking</h4><p>Videos<br>Articles</p></div>
    <div class="abs fcol" style="left:568px;top:970px"><h4>Products</h4><p>Programs<br>Mentoring</p></div>
    <div class="abs fcol" style="left:627px;top:970px"><h4>About us</h4><p>Bio</p></div>
    <div class="abs rule" style="left:435px;top:1027px;width:235px;border-top:1px solid #ccc"></div>
    <h3 class="abs section-title" style="left:435px;top:1036px">Stay connected with ewan halvorsen</h3>
    <div class="abs social" style="left:437px;top:1060px" aria-label="Email"><svg width="30" height="30"><rect x="8" y="10" width="14" height="10" fill="none" stroke="#777" stroke-width="1.5"/><path d="M8 10 L15 16 L22 10" fill="none" stroke="#777" stroke-width="1.5"/></svg></div>
    <div class="abs social" style="left:479px;top:1060px" aria-label="Social network"></div>
    <div class="abs social" style="left:521px;top:1060px" aria-label="Social network"></div>
    <div class="abs social" style="left:563px;top:1060px" aria-label="News feed"></div>

    <div class="abs foot-bar"></div>
    <p class="abs copyright">Copyright © 2012 Ewan Halvorsen. All Rights Reserved.</p>
  </footer>
</div>
</body>
</html>
```